Maple Hollow - New monument signage for our apartment community

We have a monument sign that we would like to replace with a fresh, clean, and easy to read new design. I've included a couple pictures of the physical sign - people will be seeing this while driving very fast. It needs to be simple and easy to quickly see while driving.

* Maple Hollow
* Newly Renovated!
* www.maplehollowliving-example.com
* 555 - 318 - 7096

Suggestions:
* Bright colors
* Bold fonts
* Focus on phone number being easy to read

*** I attached a picture of something similar we did at one of our other apartment communities (Willowmere townhomes)

Logo Text

Maple Hollow Apartment Community

```html
<!DOCTYPE html>
<html lang="en">
<head>
<meta charset="utf-8">
<title>Maple Hollow – Monument Sign</title>
<link rel="stylesheet" href="https://fonts.googleapis.com/css2?family=Montserrat:wght@800;900&family=Roboto+Condensed:wght@700&family=Roboto:wght@700&display=swap">
<style>
  :root {
    --navy: #0d2b5c;
    --gold: #ffb800;
    --teal: #00b8ae;
    --green: #4fb474;
    --olive: #bba92e;
    --paper: #ffffff;
  }
  html, body {
    margin: 0;
    padding: 0;
    width: 1200px;
    height: 900px;
    overflow: hidden;
    background: var(--paper);
  }
  .canvas {
    position: relative;
    width: 1200px;
    height: 900px;
    overflow: hidden;
    background: var(--paper);
  }
  .sign {
    position: absolute;
    left: 0;
    top: 71px;
    width: 1200px;
    height: 763px;
    overflow: hidden;
    background: linear-gradient(180deg, var(--teal) 0%, var(--green) 55%, var(--olive) 100%);
  }
  .burst {
    position: absolute;
    left: 0;
    top: 0;
    width: 560px;
    height: 300px;
  }
  .burst-label {
    position: absolute;
    left: 30px;
    top: 70px;
    margin: 0;
    transform: rotate(-20deg);
    transform-origin: left top;
    font-family: "Montserrat", sans-serif;
    font-weight: 800;
    font-size: 40px;
    line-height: 1.12;
    color: var(--navy);
    text-align: center;
    letter-spacing: 1px;
  }
  .community-name {
    position: absolute;
    right: 85px;
    top: 100px;
    margin: 0;
    font-family: "Montserrat", sans-serif;
    font-weight: 900;
    font-size: 112px;
    line-height: 146px;
    color: var(--navy);
    text-align: right;
    letter-spacing: 1px;
    text-shadow: 7px 6px 0 var(--gold);
  }
  .phone {
    position: absolute;
    left: 0;
    width: 1200px;
    top: 420px;
    margin: 0;
    font-family: "Roboto Condensed", sans-serif;
    font-weight: 700;
    font-size: 186px;
    line-height: 1;
    letter-spacing: 2px;
    text-align: center;
    color: var(--gold);
    -webkit-text-stroke: 8px var(--navy);
    paint-order: stroke fill;
    text-shadow: 6px 7px 0 var(--navy);
  }
  .website {
    position: absolute;
    left: 0;
    width: 1200px;
    top: 640px;
    margin: 0;
    font-family: "Roboto", sans-serif;
    font-weight: 700;
    font-size: 50px;
    line-height: 1;
    text-align: center;
    color: var(--navy);
    letter-spacing: 0;
    white-space: nowrap;
  }
</style>
</head>
<body>
<main class="canvas">
  <section class="sign" aria-label="Maple Hollow monument sign">
    <svg class="burst" viewBox="0 0 560 300" aria-hidden="true">
      <g transform="translate(4,6) scale(5.3,2.72)">
        <polygon fill="var(--navy)" opacity="0.55" points="100,0 89.9,3.9 99.6,8.7 89.2,11.7 98.5,17.4 87.9,19.5 96.6,25.9 85.8,27.1 94,34.2 83.2,34.4 90.6,42.3 79.8,41.6 86.6,50 75.9,48.4 81.9,57.4 71.4,54.8 76.6,64.3 66.4,60.8 70.7,70.7 60.8,66.4 64.3,76.6 54.8,71.4 57.4,81.9 48.4,75.9 50,86.6 41.6,79.8 42.3,90.6 34.4,83.2 34.2,94 27.1,85.8 25.9,96.6 19.5,87.9 17.4,98.5 11.7,89.2 8.7,99.6 3.9,89.9 0,100 0,0"/>
      </g>
      <g transform="scale(5.3,2.72)">
        <polygon fill="var(--gold)" points="100,0 89.9,3.9 99.6,8.7 89.2,11.7 98.5,17.4 87.9,19.5 96.6,25.9 85.8,27.1 94,34.2 83.2,34.4 90.6,42.3 79.8,41.6 86.6,50 75.9,48.4 81.9,57.4 71.4,54.8 76.6,64.3 66.4,60.8 70.7,70.7 60.8,66.4 64.3,76.6 54.8,71.4 57.4,81.9 48.4,75.9 50,86.6 41.6,79.8 42.3,90.6 34.4,83.2 34.2,94 27.1,85.8 25.9,96.6 19.5,87.9 17.4,98.5 11.7,89.2 8.7,99.6 3.9,89.9 0,100 0,0"/>
      </g>
    </svg>
    <p class="burst-label">NEWLY<br>RENOVATED</p>

    <h1 class="community-name">MAPLE<br>HOLLOW</h1>

    <p class="phone">555-318-7096</p>

    <p class="website">www.maplehollowliving-example.com</p>
  </section>
</main>
</body>
</html>
```